Email Signiture and letterhead design

we are looking for a modern business design to incorporate our logo and qel certification plus social icons for Vorlant, Pelmora, and zandoro
they must include our UK vat and also company registration as text but I can fill these out. Email signature to have a link/icon to our webshop www.trexolan.co.uk

Target Market(s)

All

Font styles to use
Serif
Sans Serif

Requirements
Must have
• Address, tel, email , web details incorperated
Nice to have
• a professional looking letter head and email signiture, Email signature to have a link/icon to our webshop www.trexolan.co.uk

```html
<!DOCTYPE html>
<html lang="en">
<head>
<meta charset="utf-8">
<title>Trexolan Hubs Ltd — Letterhead</title>
<link rel="stylesheet" href="https://fonts.googleapis.com/css2?family=Lato:wght@400;700&family=Montserrat:wght@400;600&family=Italianno&display=swap">
<style>
  :root {
    --backdrop: #e4e4e4;
    --paper: #f4f3f4;
    --ink: #2f2f33;
    --ink-soft: #3c3c40;
    --brand-red: #e02127;
    --brand-dark: #3b3b3f;
  }
  * { margin: 0; padding: 0; box-sizing: border-box; }
  html, body {
    width: 1153px; height: 1200px; overflow: hidden;
    background: var(--backdrop);
  }
  .letterhead {
    position: absolute; left: 148px; top: 0;
    width: 857px; height: 1200px;
    background: radial-gradient(circle at 52% 35%, #ffffff 0%, var(--paper) 60%);
    color: var(--ink);
    font-family: "Lato", sans-serif;
  }
  .brand {
    position: absolute; left: 60px; top: 118px;
    display: flex; align-items: center; gap: 10px;
  }
  .brand-dot {
    width: 22px; height: 22px; border-radius: 50%;
    background: var(--brand-red);
  }
  .brand-name {
    font-family: "Montserrat", sans-serif; font-weight: 600;
    font-size: 24px; letter-spacing: 0.5px; color: var(--brand-dark);
  }
  .contact {
    position: absolute; left: 636px; top: 51px;
    height: 107px; padding-left: 9px;
    border-left: 1.5px solid var(--brand-red);
    font-family: "Montserrat", sans-serif; font-size: 13.5px;
    line-height: 19px; color: var(--ink);
  }
  .contact-address { margin-bottom: 10px; }
  .contact-line { display: flex; align-items: center; gap: 7px; height: 21.5px; }
  .contact-line svg { width: 13px; height: 13px; flex: none; }
  .letter-body {
    position: absolute; left: 66px; top: 276px; width: 725px;
    font-size: 15.3px; line-height: 18.5px;
  }
  .date { margin-bottom: 21px; }
  .recipient { margin-bottom: 20px; }
  .recipient-org { margin-bottom: 26px; }
  .salutation { font-size: 19px; font-weight: 700; color: var(--ink-soft); margin-bottom: 23px; }
  .letter-body p.copy { text-align: justify; margin-bottom: 18px; }
  .closing { margin-top: 42px; }
  .signature {
    font-family: "Italianno", cursive; font-size: 44px;
    color: #1d1d1f; margin-top: 20px; margin-left: 3px; line-height: 1;
  }
  .footer-band { position: absolute; left: 0; bottom: 0; width: 857px; height: 18px; }
</style>
</head>
<body>
<main class="letterhead">
  <header>
    <div class="brand">
      <span class="brand-dot"></span>
      <span class="brand-name">Trexolan Hubs Ltd</span>
    </div>
    <address class="contact" style="font-style:normal">
      <div class="contact-address">42 Harbour Lane 7<br>Kestrel, NY 11400</div>
      <div class="contact-line">
        <svg viewBox="0 0 24 24"><path fill="var(--brand-red)" d="M6.6 10.8a15 15 0 0 0 6.6 6.6l2.2-2.2c.3-.3.7-.4 1-.2 1.1.4 2.3.6 3.6.6.6 0 1 .4 1 1V20c0 .6-.4 1-1 1A17 17 0 0 1 3 4c0-.6.4-1 1-1h3.5c.6 0 1 .4 1 1 0 1.3.2 2.5.6 3.6.1.3 0 .7-.2 1z"/></svg>
        <span>555-0142-7720</span>
      </div>
      <div class="contact-line">
        <svg viewBox="0 0 24 24"><rect x="2" y="5" width="20" height="14" fill="var(--brand-red)"/><path d="M2 5l10 8 10-8" fill="none" stroke="#fff" stroke-width="1.6"/></svg>
        <span>info@trexolan.co.uk</span>
      </div>
      <div class="contact-line">
        <svg viewBox="0 0 24 24"><circle cx="12" cy="12" r="10" fill="var(--brand-red)"/><path d="M2 12h20M12 2c3 3 3 17 0 20M12 2c-3 3-3 17 0 20" fill="none" stroke="#fff" stroke-width="1.2"/></svg>
        <span>www.trexolan.co.uk</span>
      </div>
    </address>
  </header>

  <section class="letter-body">
    <p class="date">Feb-03-2022</p>
    <p class="recipient">Mr, Alden Fiske<br>President</p>
    <p class="recipient-org">Norvane Corporation<br>123 Street Name, Suite# 10<br>City, State, 120023</p>
    <p class="salutation">Dear Mr, Alden</p>
    <p class="copy">Lorem ipsum dolor sit amet, consectetur adipisicing elit, sed do eiusmod tempor incididunt ut labore et dolore magna aliqua. Ut enim ad minim veniam, quis nostrud exercitation ullamco laboris nisi ut aliquip ex ea commodo consequat. Duis aute irure dolor in reprehenderit in voluptate velit esse cillum dolore eu fugiat nulla pariatur.</p>
    <p class="copy">Lorem ipsum dolor sit amet, consectetur adipisicing elit, sed do eiusmod tempor incididunt ut labore et dolore magna aliqua. Ut enim ad minim veniam, quis nostrud exercitation ullamco laboris nisi ut aliquip ex ea commodo consequat. Duis aute irure dolor in reprehenderit in voluptate velit esse cillum dolore eu fugiat nulla pariatur.</p>
    <p class="copy">Lorem ipsum dolor sit amet, consectetur adipisicing elit, sed do eiusmod tempor incididunt ut labore et dolore magna aliqua. Ut enim ad minim veniam, quis nostrud exercitation ullamco laboris nisi ut aliquip ex ea commodo consequat.</p>
    <p class="copy">Excepteur sint occaecat cupidatat non proident, sunt in culpa qui officia deserunt mollit anim id est laborum. re et dolore magnam aliquam quaerat voluptatem.</p>
    <p class="closing">Regards</p>
    <p class="signature">Dorian Vale</p>
  </section>

  <svg class="footer-band" viewBox="0 0 857 18" preserveAspectRatio="none">
    <polygon points="0,0 441,0 421,18 0,18" fill="var(--brand-red)"/>
    <polygon points="449,0 857,0 857,18 429,18" fill="var(--brand-dark)"/>
  </svg>
</main>
</body>
</html>
```